Brochure

I have the brochure content in this file. I would like the photos of the young people on the side, and I can add you to the dropbox folder with their photos. I would like to have the Why we are here as a tagcloud like header for like the sample attached. I would like the phrases why are we here and will you join us in bold on the tag cloud header. Here is my website www.brightharborforum.info and I would like to use the same color scheme and incorporate the whole globe/world map aspect in someho
Updates

Target Market(s)

youth, adults

Requirements
Must have
• it should use the same colors as our site
brightharborforum.info

```html
<!DOCTYPE html>
<html lang="en">
<head>
<meta charset="utf-8">
<title>2012 International Bright Harbor Forum – Brochure Front</title>
<link rel="stylesheet" href="https://fonts.googleapis.com/css2?family=Open+Sans:wght@400;600;700&family=Oswald:wght@500;600&family=Ubuntu:ital,wght@0,700;1,700&family=PT+Serif:wght@700&display=swap">
<style>
  :root {
    --sky: #9fcdfb;
    --charcoal: #3d3d3d;
    --sun: #ffed00;
    --ocean: #2f8ee0;
    --slate: #3d4c66;
    --white: #ffffff;
    --stage: #ececec;
  }
  * { box-sizing: border-box; margin: 0; padding: 0; }
  html, body { width: 1200px; height: 788px; overflow: hidden; }
  body { background: var(--stage); font-family: "Open Sans", Arial, sans-serif; position: relative; }

  .brochure {
    position: absolute; left: 42px; top: 51px; width: 1116px; height: 685px;
    display: flex; box-shadow: 0 4px 10px rgba(0,0,0,.25);
  }
  .panel { position: relative; width: 372px; height: 100%; background: var(--sky); }
  .panel + .panel { border-left: 1px solid var(--white); }
  .panel__lower {
    position: absolute; left: 0; right: 0; top: 425px; bottom: 0; background: var(--charcoal); color: var(--white);
  }

  /* Reasons panel */
  .reasons__title { position: absolute; left: 12px; top: 18px; font-size: 21px; color: var(--charcoal); font-weight: 400; }
  .reasons__list {
    position: absolute; left: 12px; top: 55px; width: 352px; list-style: none;
    color: var(--white); font-size: 15.5px; line-height: 20px; text-transform: uppercase; text-align: justify; letter-spacing: .2px;
  }
  .reasons__list li { position: relative; padding-left: 10px; }
  .reasons__list li.is-arrow::before {
    content: ""; position: absolute; left: 0; top: 6px;
    border-left: 6px solid var(--charcoal); border-top: 4px solid transparent; border-bottom: 4px solid transparent;
  }

  .event { padding: 10px 12px 0; }
  .event__year { font-size: 32px; line-height: 36px; }
  .event__intl { font-family: "PT Serif", Georgia, serif; font-weight: 700; font-size: 32px; line-height: 36px; letter-spacing: .5px; }
  .event__line { font-size: 20px; line-height: 25px; }
  .event__rule { height: 1px; background: #9aa4b0; margin: 6px 0 14px; width: 345px; }
  .event__tagline { font-family: "Ubuntu", sans-serif; font-weight: 700; font-size: 19px; line-height: 27px; padding-left: 0; }

  /* Details panel */
  .date { position: absolute; left: 15px; top: 64px; font-family: "Oswald", sans-serif; font-weight: 600; font-size: 42px; line-height: 46px; color: var(--slate); transform: scaleX(.92); transform-origin: left; }
  .pitch { position: absolute; left: 52px; top: 132px; font-size: 25px; line-height: 31px; color: var(--white); }
  .map-label { position: absolute; left: 15px; top: 272px; font-size: 21px; color: var(--charcoal); }
  .map-area {
    position: absolute; left: 16px; top: 301px; width: 339px; height: 108px;
    background: linear-gradient(135deg, #e9e5dc, #f3d68a 55%, #e8e4da); border: 1px solid #6f6f6f;
  }
  .venue { padding: 14px 15px 0; }
  .venue__title { font-size: 28px; margin-bottom: 14px; }
  .venue__row { display: flex; font-size: 17px; line-height: 22px; margin-bottom: 6px; }
  .venue__label { color: var(--sky); }

  /* Faces panel */
  .portrait { position: absolute; border: 2px solid var(--sun); }
  .portrait--one { left: 104px; top: 68px; width: 133px; height: 92px; background: linear-gradient(160deg, #7a8a55, #c9a07a); }
  .portrait--two { left: 213px; top: 168px; width: 135px; height: 93px; background: linear-gradient(160deg, #cfd6dc, #5a3c30); }
  .portrait--three { left: 108px; top: 279px; width: 133px; height: 92px; background: linear-gradient(160deg, #c88a3a, #8a6a55); }
  .brandmark {
    position: absolute; left: 3px; top: 152px; width: 248px; height: 135px; background: var(--white);
    display: flex; flex-direction: column; align-items: center; justify-content: center; gap: 8px;
  }
  .brandmark__dot { width: 46px; height: 46px; border-radius: 50%; background: var(--ocean); }
  .brandmark__name { font-size: 15px; line-height: 18px; color: var(--ocean); text-align: center; font-weight: 400; }
  .invite {
    position: absolute; left: 0; top: 456px; width: 371px; height: 129px; background: var(--sun);
    display: flex; align-items: center; justify-content: center;
  }
  .invite::before, .invite::after { content: ""; position: absolute; left: 11px; right: 11px; height: 5px; background: var(--ocean); }
  .invite::before { top: 17px; }
  .invite::after { bottom: 13px; }
  .invite__text { font-family: "Ubuntu", sans-serif; font-weight: 700; font-style: italic; font-size: 33px; color: var(--charcoal); }
</style>
</head>
<body>
  <main class="brochure">
    <section class="panel reasons">
      <h2 class="reasons__title">Why are We Here</h2>
      <ul class="reasons__list">
        <li class="is-arrow">To serve a purpose beyond myself</li>
        <li class="is-arrow">To connect</li>
        <li>For my younger siblings</li>
        <li class="is-arrow">To leave a transition fossil</li>
        <li class="is-arrow">To inspire through example...the only true leadership</li>
        <li class="is-arrow">To help people avoid mistakes that I made</li>
        <li class="is-arrow">To pave a pathway for change</li>
        <li class="is-arrow">To leave a legacy</li>
        <li class="is-arrow">To be part of a movement</li>
        <li class="is-arrow">Give back</li>
        <li class="is-arrow">Advocacy</li>
        <li class="is-arrow">To show youth that the world is what you make of it, helping to change the perspectives of how foster care is viewed.</li>
      </ul>
      <div class="panel__lower event">
        <p class="event__year">2012</p>
        <p class="event__intl">INTERNATIONAL</p>
        <p class="event__line">BRIGHT HARBOR FORUM</p>
        <p class="event__line">Multi Generational</p>
        <p class="event__line">Forum on transition awareness</p>
        <div class="event__rule"></div>
        <p class="event__tagline">From difficult transitions to breakthrough opportunities</p>
      </div>
    </section>

    <section class="panel details">
      <p class="date">June 29, 2012</p>
      <p class="pitch">We are passionate,<br>experienced and ready<br>to engage</p>
      <p class="map-label">Map</p>
      <div class="map-area" role="img" aria-label="Street map showing the forum venue location"></div>
      <div class="panel__lower venue">
        <h3 class="venue__title">Venue:</h3>
        <div class="venue__row"><span class="venue__label">Address:</span><span>Northgate University,<br>&nbsp;&nbsp;&nbsp;&nbsp;Riverton, MD</span></div>
        <div class="venue__row"><span class="venue__label">Phone:</span><span>000 000 0000</span></div>
        <div class="venue__row"><span class="venue__label">Mobile:</span><span>000 000 0000</span></div>
        <div class="venue__row"><span class="venue__label">Website:</span><span>www.brightharborforum.info</span></div>
      </div>
    </section>

    <section class="panel faces">
      <div class="portrait portrait--one" role="img" aria-label="Portrait photo of a young woman participant"></div>
      <div class="brandmark">
        <span class="brandmark__dot"></span>
        <span class="brandmark__name">2012 INTERNATIONAL<br>BRIGHT HARBOR FORUM</span>
      </div>
      <div class="portrait portrait--two" role="img" aria-label="Portrait photo of a smiling young woman participant"></div>
      <div class="portrait portrait--three" role="img" aria-label="Portrait photo of a young man participant"></div>
      <div class="invite"><p class="invite__text">Will you join us?</p></div>
    </section>
  </main>
</body>
</html>
```